Flyer design

We need a marketing flyer to use when meeting with clients. We may also use it for mailings. Please see the attached document and images. Not all images need to be used. Please feel free to edit / photoshop images. Please also see our website : www.lumivantskinlab.com

Industry/Entity Type

Marketing

```html
<!DOCTYPE html>
<html lang="en">
<head>
<meta charset="utf-8">
<title>Lumivant Dermatology &amp; Dermatopathology – Flyer</title>
<link href="https://fonts.googleapis.com/css2?family=Open+Sans:wght@400;500;600&display=swap" rel="stylesheet">
<style>
  :root {
    --paper: #e4e4e4;
    --ink: #1a1a1a;
    --accent-red: #e3242b;
    --band-blue: rgba(128, 146, 230, 0.45);
    --band-pink: rgba(236, 140, 140, 0.5);
    --panel-blue: rgba(132, 148, 232, 0.78);
    --link-blue: #3b4fd8;
    --white: #ffffff;
  }
  * { margin: 0; padding: 0; box-sizing: border-box; }
  html, body { width: 704px; height: 1200px; overflow: hidden; background: var(--paper); }
  .flyer {
    position: relative; width: 704px; height: 1200px; overflow: hidden;
    background: var(--paper);
    font-family: "Open Sans", Arial, sans-serif; color: var(--ink);
  }
  .photo-lab {
    position: absolute; left: 290px; top: 0; width: 414px; height: 1110px;
    background: linear-gradient(200deg, #2b2b2b 0%, #6a6a6a 30%, #b9b9b9 58%, #d8d8d8 72%, #8a8a8a 88%, rgba(228,228,228,0) 100%);
    opacity: 0.9;
  }
  .band { position: absolute; }
  .band-blue-top { left: 0; top: 200px; width: 704px; height: 14px; background: var(--band-blue); }
  .band-pink-top { left: 0; top: 248px; width: 704px; height: 24px; background: var(--band-pink); }
  .band-pink-mid { left: 0; top: 742px; width: 704px; height: 16px; background: var(--band-pink); }
  .rule-blue { left: 468px; top: 30px; width: 8px; height: 1080px; background: var(--band-blue); }
  .rule-pink { left: 630px; top: 0; width: 8px; height: 1200px; background: var(--band-pink); }

  .brand-mark { position: absolute; left: 108px; top: 70px; display: flex; align-items: center; gap: 12px; }
  .brand-mark .dot { width: 22px; height: 22px; border-radius: 50%; background: var(--accent-red); }
  .brand-mark .name { font-size: 44px; font-weight: 600; color: var(--ink); line-height: 1; }
  .brand-line { position: absolute; left: 42px; top: 176px; font-size: 14px; letter-spacing: 13.5px; color: var(--accent-red); }
  .brand-sub { position: absolute; left: 30px; top: 198px; font-size: 14.5px; color: var(--ink); }

  .panel { position: absolute; background: var(--panel-blue); color: var(--white); }
  .panel-services { left: 26px; top: 228px; width: 388px; height: 348px; }
  .panel-facts { left: 28px; top: 843px; width: 386px; height: 155px; }

  .headline { position: absolute; left: 40px; top: 251px; font-size: 16.5px; font-weight: 500; color: var(--ink); }
  .services-text { position: absolute; left: 40px; top: 297px; font-size: 16.5px; line-height: 27.5px; color: var(--white); white-space: nowrap; }
  .services-list { list-style: none; margin-top: 27px; }

  .stains-note { position: absolute; left: 40px; top: 627px; font-size: 16px; font-weight: 600; line-height: 25px; color: var(--ink); white-space: nowrap; }

  .physician { position: absolute; left: 40px; top: 743px; font-size: 17.5px; font-weight: 500; line-height: 27.5px; color: var(--ink); }

  .facts { position: absolute; left: 40px; top: 850px; font-size: 16.5px; color: var(--white); list-style: none; }
  .facts li { height: 56.5px; }

  .contact { position: absolute; left: 26px; top: 1127px; font-size: 13px; line-height: 21px; }
  .contact .label { color: var(--ink); }
  .contact .value { color: var(--link-blue); }
</style>
</head>
<body>
<main class="flyer">
  <div class="photo-lab" role="img" aria-label="Black and white photograph of a pathologist looking into a microscope, with a stained tissue section below"></div>

  <div class="band band-blue-top"></div>
  <div class="band band-pink-top"></div>
  <div class="band band-pink-mid"></div>
  <div class="band rule-blue"></div>
  <div class="band rule-pink"></div>

  <div class="brand-mark"><span class="dot"></span><span class="name">Lumivant</span></div>
  <div class="brand-line">LUMIVANT</div>
  <div class="brand-sub">DERMATOLOGY &amp; DERMATOPATHOLOGY</div>

  <div class="panel panel-services"></div>
  <h1 class="headline">THE DIAGNOSIS IN FOCUS</h1>
  <div class="services-text">
    <p>Commitment to helping find solutions,<br>either in-house or through our<br>contacts, for all your dermatopathology<br>&nbsp;needs including but not limited to:</p>
    <ul class="services-list">
      <li>Dermatopathology consultative service</li>
      <li>First or second opinions, off-site or on-site</li>
      <li>Tissue processing</li>
      <li>Mohs technicians</li>
      <li>Immunohistochemistry and special stains</li>
    </ul>
  </div>

  <p class="stains-note">Access to an extensive range of special and immunohistochemistry stains,<br>and patient-centered consideration of the judicious use of them.</p>

  <div class="physician">
    <p>Mara L. Quinlan, M.D.</p>
    <p>Board Certified – Dermatopathology</p>
    <p>Board Certified – Dermatology</p>
  </div>

  <div class="panel panel-facts"></div>
  <ul class="facts">
    <li>Practicing Dermatopathology since 2007</li>
    <li>2-3 day turnaround time</li>
    <li>Courier pick up services</li>
  </ul>

  <div class="contact">
    <p><span class="label">Mailing address: </span><span class="value">4120 W. Harbor Ave. #210, Seaside, CA 90999</span></p>
    <p><span class="label">Telephone: </span><span class="value">800.555.0127</span></p>
  </div>
</main>
</body>
</html>
```